Structural Engineering Firm Looking for High-Impact Lead Generation Focused Design (for B2B)

A well-established structural engineering firm in the UK wants a new website designed for them which will help them realise more business from online. Directly through the website as well as Ads and lead platforms. They need to compare favourably to competitors and have clarity. Current Site is here: http://www.quarlingpartners.example/ - you can take imagery from this site if you want to help with the design.

Target Market(s)

Homeowners, Architects, Designers, Construction Companies and Landlords

Industry/Entity Type

Professional Services

Number of Pages Required

5+ page

Font styles to use
Sans Serif

Requirements
Must have
• A Strong, Simple and Professional Design with a Focus on Lead Generation
Nice to have
• Creativity in the Detail, Clear Messaging
Should not have
• Too Much Colour, Too 'Consumer', Too Much Variation

```html
<!DOCTYPE html>
<html lang="en">
<head>
<meta charset="utf-8">
<title>Quarling Partners — Structural Engineering &amp; Party Wall Surveying</title>
<link href="https://fonts.googleapis.com/css2?family=PT+Sans:wght@400;700&display=swap" rel="stylesheet">
<style>
  :root {
    --ink: #1a1a1a;
    --heading: #333333;
    --muted: #3a3a3a;
    --rule: #d6d6d6;
    --accent: #d04545;
    --dark-pill: #444444;
    --paper: #ffffff;
    --sketch-light: #f7f7f7;
    --sketch-mid: #ececec;
    --photo-light: #e6e6e6;
    --photo-dark: #6a6a6a;
  }
  * { box-sizing: border-box; margin: 0; padding: 0; }
  html, body {
    width: 1200px; height: 625px; overflow: hidden;
    background: var(--paper);
    font-family: "PT Sans", sans-serif;
    color: var(--ink);
  }
  .page { position: relative; width: 1200px; height: 625px; }

  .site-header {
    position: absolute; left: 0; top: 0; width: 1200px; height: 95px;
    border-bottom: 1px solid var(--rule);
  }
  .brand {
    position: absolute; left: 0; top: 0; width: 322px; height: 95px;
    border-right: 1px solid var(--rule);
    display: flex; align-items: center; padding-left: 86px;
  }
  .brand-name {
    font-size: 24px; font-weight: 700; line-height: 1.05;
    color: var(--ink); letter-spacing: 0.5px; text-transform: uppercase;
  }
  .utility-nav {
    position: absolute; left: 322px; top: 0; right: 0; height: 26px;
    border-bottom: 1px solid var(--rule);
  }
  .utility-nav ul { list-style: none; position: absolute; left: 409px; top: 0; display: flex; height: 26px; }
  .utility-nav li {
    width: 96px; height: 26px; border-left: 1px solid var(--rule);
    display: flex; align-items: center; justify-content: center;
    font-size: 11px; color: var(--ink);
  }
  .utility-nav li:last-child { border-right: 1px solid var(--rule); }
  .main-nav ul { list-style: none; }
  .main-nav li {
    position: absolute; top: 50px; font-size: 16.5px; color: var(--ink);
  }
  .main-nav li.is-active { color: var(--accent); }

  .hero { position: absolute; left: 0; top: 96px; width: 1200px; height: 436px; }
  .hero-sketch {
    position: absolute; left: 38px; top: 0; width: 700px; height: 436px;
    background: linear-gradient(100deg, var(--sketch-light) 0%, var(--sketch-mid) 55%, var(--paper) 100%);
    opacity: 0.8;
  }
  .hero-photo { position: absolute; left: 0; top: 0; }

  .hero-copy { position: absolute; left: 86px; top: 108px; width: 440px; }
  .hero-title {
    font-size: 24.5px; font-weight: 700; line-height: 35px; color: var(--heading);
  }
  .hero-lede { margin-top: 14px; font-size: 16px; color: var(--muted); }

  .hero-actions { position: absolute; left: 86px; top: 288px; display: flex; gap: 23px; }
  .service-select {
    width: 255px; height: 37px; border-radius: 19px; background: var(--dark-pill);
    color: var(--paper); font-size: 14.5px; display: flex; align-items: center;
    padding-left: 29px; gap: 18px;
  }
  .quote-button {
    width: 107px; height: 37px; border-radius: 19px; background: var(--accent);
    color: var(--paper); font-size: 14.5px; display: flex; align-items: center; justify-content: center;
  }
</style>
</head>
<body>
<div class="page">
  <header class="site-header">
    <div class="brand"><span class="brand-name">Quarling<br>Partners</span></div>
    <nav class="utility-nav">
      <ul><li>Gallery</li><li>Blog</li><li>About us</li><li>Contact us</li></ul>
    </nav>
    <nav class="main-nav">
      <ul>
        <li class="is-active" style="left:567px">Engineering</li>
        <li style="left:699px">Party Wall</li>
        <li style="left:820px">Planning</li>
        <li style="left:929px">Surveys</li>
        <li style="left:1034px">Partners</li>
      </ul>
    </nav>
  </header>

  <section class="hero">
    <div class="hero-sketch" role="img" aria-label="Faint architectural line drawing of a modern multi-storey building"></div>
    <svg class="hero-photo" width="1200" height="436" viewBox="0 0 1200 436" role="img" aria-label="Black and white photograph of a round museum reading room under a glass lattice roof, with visitors on the stairs">
      <defs>
        <linearGradient id="photoTone" x1="0" y1="0" x2="1" y2="1">
          <stop offset="0" stop-color="var(--photo-dark)"/>
          <stop offset="0.45" stop-color="var(--photo-light)"/>
          <stop offset="1" stop-color="var(--photo-dark)"/>
        </linearGradient>
      </defs>
      <polygon points="724,0 1200,0 1200,436 720,436 573,206" fill="url(#photoTone)"/>
    </svg>

    <div class="hero-copy">
      <h1 class="hero-title">Efficient and Professional Structural Engineering and Party Wall Surveying</h1>
      <p class="hero-lede">Get a Competitive Quote from the local experts</p>
    </div>

    <div class="hero-actions">
      <div class="service-select">What Service are looking for ?
        <svg width="11" height="8" viewBox="0 0 11 8" aria-hidden="true"><polygon points="0,0 11,0 5.5,8" fill="#ffffff"/></svg>
      </div>
      <div class="quote-button">Get a Quote</div>
    </div>
  </section>
</div>
</body>
</html>
```